General contractor/GM consaltant business card

I need a card for my contracting company in North Dakota, we build industrial buildings for the oil feild and oil feild related companies offices, shops, airplain hangars, airports ext. We have a familly atmosphere on the job and are very relational and personal.
Industry/Entity Type
Industrial
Contact Information for Business Card
Kestrelmoor Builders LLC.
Dwight T.Halvorsun
4736 Quillfern dr. Colorado Springs, CO. 80927
Cell# 406-555-8142
dwight@kestrelmoorbuilders.com

```html
<!DOCTYPE html>
<html lang="en">
<head>
<meta charset="utf-8">
<title>Kestrelmoor Builders LLC. – Business Card</title>
<link rel="stylesheet" href="https://fonts.googleapis.com/css2?family=Signika:wght@600;700&display=swap">
<style>
  :root {
    --stage: #d6d6d6;
    --ink: #141414;
    --card-dark: #2b2b2b;
    --mark-grey: #3a3a3a;
    --white: #ffffff;
    --photo-light: #e9c48a;
    --photo-dark: #8a5a2c;
  }
  * { margin: 0; padding: 0; box-sizing: border-box; }
  html, body { width: 1200px; height: 759px; overflow: hidden; }
  body {
    background: var(--stage);
    font-family: "Signika", "Trebuchet MS", sans-serif;
    position: relative;
  }
  .card {
    position: absolute;
    width: 645px;
    height: 380px;
    border-radius: 12px;
    overflow: hidden;
    box-shadow: 0 6px 18px rgba(0,0,0,.25);
  }
  .card--front { left: 45px; top: 45px; }
  .card--back { left: 480px; top: 330px; background: var(--card-dark); }

  .front-photo {
    position: absolute;
    inset: 0;
    background: linear-gradient(180deg, var(--photo-light) 0%, var(--photo-dark) 100%);
  }

  .wordmark {
    position: absolute;
    display: flex;
    align-items: center;
    gap: 22px;
  }
  .wordmark__square {
    width: 92px;
    height: 92px;
    flex: none;
  }
  .wordmark__name {
    font-weight: 700;
    font-size: 56px;
    line-height: 0.95;
    letter-spacing: -0.5px;
  }
  .card--front .wordmark { left: 62px; top: 88px; }
  .card--front .wordmark__square { background: var(--ink); }
  .card--front .wordmark__name { color: var(--ink); }

  .card--back .wordmark { left: 52px; top: 62px; }
  .card--back .wordmark__square { background: var(--mark-grey); }
  .card--back .wordmark__name { color: var(--white); font-size: 58px; }

  .contact {
    position: absolute;
    left: 32px;
    top: 205px;
    color: var(--white);
    font-style: normal;
  }
  .contact__name {
    font-size: 21px;
    font-weight: 700;
    letter-spacing: .3px;
    margin-bottom: 6px;
  }
  .contact__line {
    font-size: 12.5px;
    font-weight: 600;
    line-height: 1.55;
    letter-spacing: .2px;
  }
</style>
</head>
<body>
  <section class="card card--front" aria-label="Business card front">
    <div class="front-photo" role="img" aria-label="Photograph of an oil field at sunset"></div>
    <div class="wordmark">
      <span class="wordmark__square" aria-hidden="true"></span>
      <h1 class="wordmark__name">Kestrelmoor<br>Builders LLC.</h1>
    </div>
  </section>

  <section class="card card--back" aria-label="Business card back">
    <div class="wordmark">
      <span class="wordmark__square" aria-hidden="true"></span>
      <h2 class="wordmark__name">Kestrelmoor<br>Builders LLC.</h2>
    </div>
    <address class="contact">
      <p class="contact__name">Dwight T.Halvorsun</p>
      <p class="contact__line">4736 Quillfern dr.</p>
      <p class="contact__line">Colorado Springs, CO. 80927</p>
      <p class="contact__line">Cell# 406-555-8142</p>
      <p class="contact__line">dwight@kestrelmoorbuilders.com</p>
    </address>
  </section>
</body>
</html>
```